Valbrook Data Works

Our company is about IT hardwares and IT solutions. IT hardware such as PC, RAMS, storage and servers. IT solutions such as project management, BA. We are also selling new technology too.

Target Market(s)

Consumer, Small to Medium Business, Corporate

Requirements
Must have
• The business card must have the following:
• Name:
• Title:
• Contact Number:
• Email address:
• Website:
• Color: Must match the logo color upgrade

```html
<!DOCTYPE html>
<html lang="en">
<head>
<meta charset="utf-8">
<title>Valbrook Data Works – Business Card</title>
<link href="https://fonts.googleapis.com/css2?family=Open+Sans:wght@400;600;800&display=swap" rel="stylesheet">
<style>
  :root {
    --backdrop: #2a2a2a;
    --card: #111111;
    --card-edge: #1b1b1b;
    --accent: #e08a2a;
    --accent-dark: #b9651b;
    --accent-light: #f3a94a;
    --text-light: #f2f2f2;
    --text-muted: #bdbdbd;
    --divider: #6a6a6a;
  }
  * { box-sizing: border-box; margin: 0; padding: 0; }
  html, body {
    width: 1200px; height: 900px; overflow: hidden;
    background: var(--backdrop);
    font-family: "Open Sans", Arial, sans-serif;
  }
  .stage { position: relative; width: 1200px; height: 900px; }
  .card {
    position: absolute;
    left: 310px;
    width: 580px; height: 330px;
    background: linear-gradient(160deg, var(--card-edge), var(--card));
    overflow: hidden;
    box-shadow: 0 14px 30px rgba(0,0,0,.45);
  }
  .card--front { top: 75px; }
  .card--back { top: 480px; }
  .card__band {
    position: absolute; left: 0; right: 0; bottom: 0; height: 9px;
    background: linear-gradient(90deg, var(--accent-dark), var(--accent-light), var(--accent));
  }
  .brand {
    position: absolute; inset: 0 0 9px 0;
    display: flex; flex-direction: column; align-items: center; justify-content: center; gap: 16px;
  }
  .brand__dot {
    width: 34px; height: 34px; border-radius: 50%;
    background: var(--accent);
  }
  .brand__name {
    color: var(--text-light);
    font-weight: 800; font-size: 34px; letter-spacing: 1px;
    text-transform: uppercase;
  }
  .person {
    position: absolute; left: 0; width: 262px; top: 128px;
    text-align: right;
  }
  .person__name {
    color: var(--accent);
    font-size: 19px; font-weight: 400; letter-spacing: .5px;
    text-transform: uppercase;
  }
  .person__title {
    color: var(--text-muted);
    font-size: 15px; margin-top: 2px;
  }
  .divider {
    position: absolute; left: 284px; top: 118px;
    width: 1px; height: 72px; background: var(--divider);
  }
  .contacts {
    position: absolute; left: 306px; top: 122px;
    list-style: none;
    display: flex; flex-direction: column; gap: 8px;
  }
  .contacts__item {
    display: flex; align-items: center; gap: 8px;
    color: var(--text-light); font-size: 15px;
  }
  .contacts__icon { width: 20px; height: 20px; flex: none; }
</style>
</head>
<body>
<div class="stage">
  <section class="card card--front">
    <div class="brand">
      <span class="brand__dot"></span>
      <span class="brand__name">Valbrook Data Works</span>
    </div>
    <div class="card__band"></div>
  </section>

  <section class="card card--back">
    <div class="person">
      <p class="person__name">Marcus Hale</p>
      <p class="person__title">Managing Director</p>
    </div>
    <div class="divider"></div>
    <ul class="contacts">
      <li class="contacts__item">
        <svg class="contacts__icon" viewBox="0 0 20 20" aria-hidden="true">
          <circle cx="10" cy="10" r="10" fill="var(--accent)"/>
          <path d="M6.5 5.5c.6-.4 1.2-.3 1.5.2l.9 1.6c.3.5.1 1-.3 1.3l-.6.4c.5 1.2 1.4 2.1 2.6 2.6l.4-.6c.3-.4.8-.6 1.3-.3l1.6.9c.5.3.6.9.2 1.5-.6.9-1.6 1.3-2.6.9C8.9 13 7 11.1 6 8.5c-.4-1 0-2.2.5-3z" fill="#111"/>
        </svg>
        <span>044-555 012 347</span>
      </li>
      <li class="contacts__item">
        <svg class="contacts__icon" viewBox="0 0 20 20" aria-hidden="true">
          <circle cx="10" cy="10" r="10" fill="var(--accent)"/>
          <rect x="5" y="6.5" width="10" height="7" rx="1" fill="#111"/>
          <path d="M5.5 7l4.5 3.5L14.5 7" fill="none" stroke="var(--accent)" stroke-width="1"/>
        </svg>
        <span>info@valbrookdata.com</span>
      </li>
      <li class="contacts__item">
        <svg class="contacts__icon" viewBox="0 0 20 20" aria-hidden="true">
          <circle cx="10" cy="10" r="10" fill="var(--accent)"/>
          <circle cx="10" cy="10" r="5" fill="none" stroke="#111" stroke-width="1.4"/>
          <path d="M5 10h10M10 5c-2 2.8-2 7.2 0 10M10 5c2 2.8 2 7.2 0 10" fill="none" stroke="#111" stroke-width="1.1"/>
        </svg>
        <span>www.valbrookdata.com</span>
      </li>
    </ul>
    <div class="card__band"></div>
  </section>
</div>
</body>
</html>
```